Havenry - "Where Pest Control is Free for Life..." Please see pitch deck...

Project goal, that this is a reusable template, not a one-off card
Brand and design direction, follow the logo, use the brand palette (with a color swatch table), typography and layout guidance
The Mark Vale placeholder content as a clean field-by-field table (name, title, company, address, office, cell, fax, email, havenry.com)
Print specs, 3.5 × 2 in trim, 0.125 in bleed, 300 DPI, CMYK, crop marks
Deliverables, layered editable PSD (your primary ask) plus vector .AI/.EPS and a press-ready PDF/X-1a, with fonts packaged
What you'll provide (logo, colors, fonts)
Process and sign-off, concept first, then full file package on approval.
Populate every field with this Mark Vale placeholder data so we can see the layout fully built out. We will replace it per person.
Name Mark Vale
Title Title / Position
Company Havenry
Address 487 Orchard Lane, Suite 210, Tallahassee, FL 32308
Office (850) 555-0142
Cell (850) 555-0167
Fax (850) 555-0181
Email markvale@havenry.com
Website havenry.com

We need the working, editable source files so we can update them ourselves, plus a ready-to-print export:
1. Photoshop (.PSD) — fully layered and editable, with each contact field on its own labeled text layer. This is the primary requested format.
2. Vector source — the press-standard editable format, Adobe Illustrator (.AI) and/or .EPS, since vector is preferred for crisp text and logos at print.
3. Print-ready PDF — press-quality (PDF/X-1a), CMYK, with bleed and crop marks, both sides.
4. Packaged fonts and links — include or list all fonts used, and package any linked assets so the files open correctly on our end.

Why both PSD and vector
The PSD covers our request directly and is easy for us to edit. Vector (.AI/.EPS) is what most commercial printers actually prefer for type and logos because it stays razor-sharp at any size. Providing both keeps us flexible no matter which printer we use. Have fun and keep it modern and cool the designer of the logo did a great job, see what you can do.

```html
<!DOCTYPE html>
<html lang="en">
<head>
<meta charset="utf-8">
<title>Havenry Business Card</title>
<link rel="stylesheet" href="https://fonts.googleapis.com/css2?family=Montserrat:wght@400;600;800&family=Lato:wght@400&display=swap">
<style>
  :root {
    --page-bg: #1c1c1c;
    --card-bg: #1a1a1a;
    --teal: #10b3c6;
    --white: #ffffff;
    --ink-dark: #111111;
    --pattern-dark: #0b0b0b;
    --pattern-light: #5a5a5a;
  }
  * { margin: 0; padding: 0; box-sizing: border-box; }
  html, body {
    width: 1200px;
    height: 1059px;
    overflow: hidden;
    background: var(--page-bg);
  }
  .canvas { position: relative; width: 1200px; height: 1059px; }

  .card {
    position: absolute;
    left: 255px;
    width: 692px;
    height: 394px;
    border-radius: 18px;
    overflow: hidden;
  }
  .card-front { top: 87px; background: var(--card-bg); }
  .card-back {
    top: 547px;
    background: linear-gradient(90deg, var(--pattern-dark) 0%, #141414 45%, #3a3a3a 75%, var(--pattern-light) 100%);
  }

  .brand {
    position: absolute;
    left: 0; right: 0; top: 52px;
    display: flex;
    justify-content: center;
    align-items: center;
    gap: 14px;
  }
  .brand-mark {
    width: 40px; height: 40px;
    background: var(--teal);
    border-radius: 4px;
  }
  .brand-name {
    font-family: 'Montserrat', sans-serif;
    font-weight: 800;
    font-size: 76px;
    letter-spacing: -2px;
    color: var(--white);
    line-height: 1;
  }

  .identity {
    position: absolute;
    right: 482px; top: 206px;
    text-align: right;
    font-family: 'Montserrat', sans-serif;
  }
  .person-name {
    font-weight: 600;
    font-size: 27px;
    color: var(--teal);
    letter-spacing: 0.5px;
    line-height: 1.1;
  }
  .person-title {
    font-weight: 400;
    font-size: 19px;
    color: var(--white);
    margin-top: 4px;
  }

  .divider {
    position: absolute;
    top: 207px;
    width: 2px; height: 57px;
    background: var(--teal);
  }
  .divider-one { left: 228px; }
  .divider-two { left: 413px; }

  .contact-list {
    position: absolute;
    list-style: none;
    font-family: 'Lato', sans-serif;
    font-size: 19.5px;
    color: var(--white);
  }
  .contact-list li {
    display: flex;
    align-items: center;
    height: 27px;
  }
  .contact-list svg { flex: none; fill: var(--teal); }
  .contact-phones { left: 240px; top: 206px; }
  .contact-phones svg { margin-right: 8px; width: 18px; height: 18px; }
  .contact-other { left: 424px; top: 204px; }
  .contact-other svg { margin-right: 10px; width: 20px; height: 18px; }

  .address {
    position: absolute;
    left: 0; right: 0; top: 297px;
    display: flex;
    justify-content: center;
    align-items: center;
    gap: 14px;
    font-family: 'Lato', sans-serif;
    font-size: 19.5px;
    color: var(--white);
  }
  .address svg { fill: var(--teal); width: 17px; height: 22px; }

  .footer-band { position: absolute; left: 0; bottom: 0; width: 692px; height: 31px; }
  .website {
    position: absolute;
    left: 470px; width: 140px; bottom: 4px;
    font-family: 'Lato', sans-serif;
    font-size: 18px;
    color: var(--ink-dark);
    text-align: center;
    white-space: nowrap;
  }
</style>
</head>
<body>
<main class="canvas">

  <section class="card card-front" aria-label="Business card front">
    <div class="brand">
      <span class="brand-name">Havenry</span>
      <span class="brand-mark" aria-hidden="true"></span>
    </div>

    <div class="identity">
      <p class="person-name">MARK VALE</p>
      <p class="person-title">Owner</p>
    </div>

    <span class="divider divider-one"></span>
    <span class="divider divider-two"></span>

    <ul class="contact-list contact-phones">
      <li>
        <svg viewBox="0 0 24 24" aria-hidden="true"><path d="M2 9c0-3 5-5 10-5s10 2 10 5v2h-5V8.5c-1.5-.6-3.3-.9-5-.9s-3.5.3-5 .9V11H2zM6 12l2-3h8l2 3v7H6z"/></svg>
        (850) 555-0142
      </li>
      <li>
        <svg viewBox="0 0 24 24" aria-hidden="true"><path d="M7 1h10a2 2 0 0 1 2 2v18a2 2 0 0 1-2 2H7a2 2 0 0 1-2-2V3a2 2 0 0 1 2-2zm0 3v14h10V4zm5 15.5a1.2 1.2 0 1 0 0 2.4 1.2 1.2 0 0 0 0-2.4z"/></svg>
        (850) 555-0167
      </li>
    </ul>

    <ul class="contact-list contact-other">
      <li>
        <svg viewBox="0 0 24 22" aria-hidden="true"><path d="M1 6h4v15H1zM7 2h10v5h4a2 2 0 0 1 2 2v12H7zm2 2v3h6V4zm2 6v2h2v-2zm4 0v2h2v-2zm4 0v2h2v-2zm-8 4v2h2v-2zm4 0v2h2v-2zm4 0v2h2v-2z"/></svg>
        (850) 555-0181
      </li>
      <li>
        <svg viewBox="0 0 24 18" aria-hidden="true"><path d="M1 1h22v2l-11 7L1 3zm0 4l11 7 11-7v12H1z"/></svg>
        markvale@havenry.com
      </li>
    </ul>

    <p class="address">
      <svg viewBox="0 0 16 22" aria-hidden="true"><path d="M8 0a8 8 0 0 1 8 8c0 6-8 14-8 14S0 14 0 8a8 8 0 0 1 8-8zm0 4.5a3.5 3.5 0 1 0 0 7 3.5 3.5 0 0 0 0-7z"/></svg>
      487 Orchard Lane, Suite 210, Tallahassee, FL 32308
    </p>

    <svg class="footer-band" viewBox="0 0 692 31" aria-hidden="true">
      <polygon points="0,9 393,9 388,15 0,15" fill="var(--teal)"/>
      <polygon points="414,0 692,0 692,31 0,31 0,24 384,24" fill="var(--teal)"/>
    </svg>
    <p class="website">www.havenry.com</p>
  </section>

  <section class="card card-back" role="img" aria-label="Card back: repeating pattern of house-shaped brand tiles fading from black on the left to grey on the right"></section>

</main>
</body>
</html>
```